Corvimo Business Card

Corvimo is a young and energetic software development consultancy. We spend our time on the road working with clients on their sites an meeting new potential customers and employees!

We need a sharp, vibrant and memorable business card that will inspires those that receive it to look after it as it oozes quality and is a nice thing in its own right.

We like bold colours and distinctive design. So show us what you can do.

In terms of information on the card, it would be good to see:

* Our logo (Obviously :) )
* Employee name
* Email
* Website address
* Mobile number
* Full company name (Corvimo ltd)
* Registered company number
* Registered company address

Industry/Entity Type

Software

Requirements
Nice to have
• We are thinking that having a QR Code on the business card could be a good way of adding active marketing. It would be good to see if you are able to merge the kind of element in to your designs!

Maybe something special could be achieved using a visual QR Code like those produced at http://www.pixoranta.example/ ? You have our media so feel free to have a play.

```html
<!DOCTYPE html>
<html lang="en">
<head>
<meta charset="utf-8">
<title>Corvimo Business Card</title>
<link rel="stylesheet" href="https://fonts.googleapis.com/css2?family=Titillium+Web:wght@400;600&display=swap">
<style>
  :root {
    --card-bg: #202324;
    --row-bg: #262a2c;
    --brand-red: #c62f31;
    --ink-light: #ffffff;
    --logo-grey: #9ea3a8;
    --page-bg: #ffffff;
  }
  * { box-sizing: border-box; margin: 0; padding: 0; }
  html, body { width: 1200px; height: 927px; overflow: hidden; background: var(--page-bg); }
  body { position: relative; font-family: "Titillium Web", sans-serif; color: var(--ink-light); }

  .card {
    position: absolute; top: 32px; width: 549px; height: 846px;
    background: var(--card-bg); overflow: hidden;
  }
  .card--front { left: 36px; }
  .card--back { left: 616px; }

  .wordmark {
    position: absolute; top: 58px; left: 0; width: 100%;
    text-align: center; font-size: 80px; font-weight: 400;
    letter-spacing: 4px; line-height: 1; color: var(--logo-grey);
  }

  .name-band {
    position: absolute; left: 38px; width: 474px; height: 82px;
    background: var(--brand-red);
    display: flex; align-items: center; justify-content: center; gap: 32px;
    line-height: 1;
  }
  .card--front .name-band { top: 383px; }
  .card--back .name-band { top: 167px; }
  .name-band__name { font-size: 30px; font-weight: 600; letter-spacing: 1.5px; }
  .name-band__role { font-size: 20px; font-weight: 400; letter-spacing: 1px; padding-top: 4px; }

  .front-site {
    position: absolute; top: 742px; left: 0; width: 100%;
    text-align: center; font-size: 33px; letter-spacing: 1.5px; line-height: 1;
  }

  .footer-band {
    position: absolute; left: 0; bottom: 0; width: 100%; height: 51px;
    background: var(--brand-red);
  }

  .contact-list { position: absolute; left: 36px; top: 289px; width: 477px; list-style: none; }
  .contact-row {
    display: flex; height: 80px; margin-bottom: 18px;
  }
  .contact-row__icon {
    width: 71px; height: 80px; flex: none; background: var(--brand-red);
    display: flex; align-items: center; justify-content: center;
  }
  .contact-row__icon svg { width: 42px; height: 42px; }
  .contact-row__text {
    flex: 1; background: var(--row-bg); display: flex; align-items: center;
    padding-left: 37px; font-size: 26px; letter-spacing: 1.2px; line-height: 1.3;
    white-space: nowrap;
  }
</style>
</head>
<body>

<section class="card card--front">
  <div class="wordmark">CORVIMO</div>
  <div class="name-band">
    <span class="name-band__name">JOHN DOE</span>
    <span class="name-band__role">CEO MANAGER</span>
  </div>
  <div class="front-site">www.corvimo.example</div>
  <div class="footer-band"></div>
</section>

<section class="card card--back">
  <div class="wordmark">CORVIMO</div>
  <div class="name-band">
    <span class="name-band__name">JOHN DOE</span>
    <span class="name-band__role">CEO MANAGER</span>
  </div>

  <ul class="contact-list">
    <li class="contact-row">
      <span class="contact-row__icon">
        <svg viewBox="0 0 40 40" fill="none" stroke="#fff" stroke-width="2.5">
          <rect x="11" y="3" width="18" height="34" rx="3"/>
          <line x1="11" y1="9" x2="29" y2="9"/>
          <line x1="11" y1="29" x2="29" y2="29"/>
          <circle cx="20" cy="33" r="1.2" fill="#fff"/>
        </svg>
      </span>
      <span class="contact-row__text">+91 9812045670</span>
    </li>
    <li class="contact-row">
      <span class="contact-row__icon">
        <svg viewBox="0 0 40 40" fill="none" stroke="#fff" stroke-width="2.2">
          <rect x="3" y="9" width="34" height="22"/>
          <polyline points="3,9 20,23 37,9"/>
          <polyline points="3,31 16,19"/>
          <polyline points="37,31 24,19"/>
        </svg>
      </span>
      <span class="contact-row__text">employee@corvimo.example</span>
    </li>
    <li class="contact-row">
      <span class="contact-row__icon">
        <svg viewBox="0 0 40 40">
          <path d="M20 2a12 12 0 0 0-12 12c0 9 12 24 12 24s12-15 12-24A12 12 0 0 0 20 2z" fill="#fff"/>
          <circle cx="20" cy="14" r="4.5" fill="#c62f31"/>
        </svg>
      </span>
      <span class="contact-row__text">Orvel 412, UK K4R,<br>Mill Lane, SE</span>
    </li>
    <li class="contact-row">
      <span class="contact-row__icon">
        <svg viewBox="0 0 40 40" fill="#fff">
          <path d="M3 16c0-5 8-8 17-8s17 3 17 8v3h-8v-4c-3-1-6-1.5-9-1.5s-6 .5-9 1.5v4H3z"/>
          <path d="M13 20h14l3 12H10z"/>
          <circle cx="20" cy="26" r="3.5" fill="#c62f31"/>
        </svg>
      </span>
      <span class="contact-row__text">+36 418207</span>
    </li>
    <li class="contact-row">
      <span class="contact-row__icon">
        <svg viewBox="0 0 40 40" fill="none" stroke="#fff" stroke-width="2.2">
          <circle cx="20" cy="20" r="17"/>
          <ellipse cx="20" cy="20" rx="8" ry="17"/>
          <line x1="20" y1="3" x2="20" y2="37"/>
          <line x1="3" y1="20" x2="37" y2="20"/>
          <path d="M6 11h28M6 29h28"/>
        </svg>
      </span>
      <span class="contact-row__text">www.corvimo.example</span>
    </li>
  </ul>

  <div class="footer-band"></div>
</section>

</body>
</html>
```